Saucy Velvet Impz Business Card

We need business cards designed for our consultants to use and hand out to customers.
We are an Adult party plan company (like Crelvaware but sex toys and lingerie)
We would like bright colours pinks, purples.
The cards need our logo
Space for the reps phone number email address and name.
We need our website on it www.saucyvelvetimps.com.au

```html
<!DOCTYPE html>
<html lang="en">
<head>
<meta charset="utf-8">
<title>Saucy Velvet Impz Parties – Business Card</title>
<link rel="stylesheet" href="https://fonts.googleapis.com/css2?family=Arimo:wght@400;700&family=Kaushan+Script&display=swap">
<style>
  :root {
    --canvas: #c9c9cb;
    --card-deep: #8e1561;
    --card-mid: #c02c85;
    --card-light: #d869a8;
    --photo-warm: #d98aa8;
    --photo-deep: #9c3b7a;
    --hot-pink: #ff2e97;
    --white: #ffffff;
    --shadow: rgba(40, 20, 40, 0.28);
  }
  * { box-sizing: border-box; margin: 0; padding: 0; }
  html, body { width: 1200px; height: 900px; overflow: hidden; }
  body {
    background: var(--canvas);
    font-family: "Arimo", Arial, sans-serif;
    color: var(--white);
    position: relative;
  }
  .card {
    position: absolute;
    left: 320px;
    width: 560px;
    height: 311px;
    border-radius: 3px;
    overflow: hidden;
    box-shadow: 0 10px 24px var(--shadow);
  }
  .card--front {
    top: 119px;
    background:
      radial-gradient(circle at 70% 40%, var(--card-light) 0%, transparent 55%),
      linear-gradient(135deg, var(--card-mid) 0%, var(--card-deep) 100%);
  }
  .card--back {
    top: 470px;
    background:
      radial-gradient(circle at 35% 35%, var(--card-light) 0%, transparent 50%),
      linear-gradient(160deg, var(--card-mid) 0%, var(--card-deep) 100%);
  }
  .tagline {
    position: absolute;
    left: 28px;
    top: 56px;
    font-weight: 700;
    font-size: 22px;
    letter-spacing: 0.2px;
  }
  .party-photo {
    position: absolute;
    right: 0;
    top: 0;
    width: 300px;
    height: 190px;
    background: radial-gradient(ellipse at 50% 45%, var(--photo-warm) 0%, var(--photo-deep) 70%, transparent 100%);
  }
  .brand {
    position: absolute;
    display: flex;
    align-items: center;
    gap: 12px;
    font-weight: 700;
    color: var(--white);
    white-space: nowrap;
  }
  .brand__dot {
    width: 34px;
    height: 34px;
    border-radius: 50%;
    background: var(--hot-pink);
    flex: none;
  }
  .card--front .brand { left: 30px; bottom: 38px; font-size: 30px; }
  .card--back .brand { left: 40px; top: 62px; font-size: 26px; }
  .card--back .brand__dot { width: 28px; height: 28px; }
  .rep {
    position: absolute;
    left: 150px;
    top: 150px;
  }
  .rep__name {
    font-family: "Kaushan Script", cursive;
    font-size: 24px;
    line-height: 1.2;
  }
  .rep__email { font-size: 14px; margin-top: 4px; }
  .rep__email-label { color: var(--hot-pink); }
  .booking {
    position: absolute;
    left: 150px;
    top: 226px;
  }
  .booking__line { font-size: 15px; }
  .booking__phone {
    font-family: "Kaushan Script", cursive;
    font-size: 30px;
    line-height: 1.2;
  }
</style>
</head>
<body>
  <section class="card card--front" aria-label="Card front">
    <div class="party-photo" role="img" aria-label="Photo of a group of women celebrating with cocktails"></div>
    <p class="tagline">Australia’s #1 Adult Party Plan</p>
    <div class="brand"><span class="brand__dot"></span>Saucy Velvet Impz Parties</div>
  </section>

  <section class="card card--back" aria-label="Card back">
    <div class="brand"><span class="brand__dot"></span>Saucy Velvet Impz Parties</div>
    <div class="rep">
      <p class="rep__name">Jasmine Calder</p>
      <p class="rep__email"><span class="rep__email-label">Email:</span> info@saucyvelvetimps.com.au</p>
    </div>
    <div class="booking">
      <p class="booking__line">Book your Saucy Velvet Impz party today...</p>
      <p class="booking__phone">0491 570 156</p>
    </div>
  </section>
</body>
</html>
```